Bright Horizon Painting and Remodeling needs a business card

Business card should have company logo. I will upload two different logos and let me see which one is a better design for the business card.

Name of company: Bright Horizon Painting and Remodeling
Address: 4126 NW 71st st Suite 214
Miami, FL 33166

local phone: (305) 555-0142
toll free (855) 555-0197
fax (866) 555-0163

email: corinne@paintingbrighthorizon.example

not sure if i should include social media links or names on the business card.

company does interior and exterior painting, pressure washing, wall paper removal, drywall and stucco repair, staining,

We give free estimates.

I want a two sided business card.

Not sure if all this information is necessary for the business card. Designer can pick out whatever information they deem is important for a consumer to see on the business card.

Anticipating on the business card to be printed on nice quality.

I will upload an image of one of the logos on a type of business card surface. That idea can be used as well. Be creative. Business card should be professional but very nice and eye catching.

remove drywall and stucco repair and replace with tile installation

Industry/Entity Type

Business

Contact Information for Business Card

Miami, FL 33166

toll free (855) 555-0197
fax (866) 555-0163

company does interior and exterior painting, pressure washing, wall paper removal, drywall and stucco repair, staining, tile removal, *specializing in vinyl floor removal

free estimates.

Requirements
Must have
• Profesional font

```html
<!DOCTYPE html>
<html lang="en">
<head>
<meta charset="utf-8">
<title>Bright Horizon Painting and Remodeling – Business Card</title>
<link href="https://fonts.googleapis.com/css2?family=Roboto:wght@400;500&family=Roboto+Condensed:wght@400;700&family=Roboto+Slab:wght@500;700&display=swap" rel="stylesheet">
<style>
  :root {
    --bg: #e9e6e2;
    --card-white: #ffffff;
    --card-black: #0c0c0c;
    --ink-red: #e0202a;
    --ink-gray: #6b6b6b;
    --ink-text: #7a7a7a;
    --divider: #9a9a9a;
    --c-yellow: #f1d43a;
    --c-orange: #ef5a2a;
    --c-magenta: #b2247f;
    --c-purple: #6a2c8a;
    --c-blue: #1f6fb8;
    --s-lime: #c6dc45;
    --s-yellow: #f4e46a;
    --s-orange: #f0582f;
    --s-pink: #c8287f;
    --s-blue: #3a90c6;
    --logo-ink: #333333;
  }
  * { box-sizing: border-box; margin: 0; padding: 0; }
  html, body { width: 1200px; height: 1000px; overflow: hidden; }
  body { background: var(--bg); position: relative; font-family: "Roboto", Arial, sans-serif; }

  .card { position: absolute; width: 580px; height: 330px; box-shadow: 0 6px 18px rgba(0,0,0,.18); }

  /* Front */
  .card-front { left: 120px; top: 150px; background: var(--card-white); display: flex; align-items: center; }
  .brand-mark { width: 250px; display: flex; flex-direction: column; align-items: center; gap: 14px; }
  .brand-mark__dot { width: 70px; height: 70px; border-radius: 50%; background: var(--logo-ink); }
  .brand-mark__name { font-family: "Roboto Slab", Georgia, serif; font-weight: 700; font-size: 22px; color: var(--logo-ink); text-align: center; line-height: 1.2; }
  .divider { width: 1px; height: 185px; background: var(--divider); }
  .details { padding-left: 26px; }
  .company-name { font-family: "Roboto Slab", Georgia, serif; font-weight: 700; font-size: 28px; color: var(--ink-red); line-height: 1; }
  .company-tagline { font-family: "Roboto", Arial, sans-serif; font-weight: 500; font-size: 16px; color: var(--ink-gray); margin-top: 2px; }
  .contact-list { list-style: none; margin-top: 22px; }
  .contact-list li { display: flex; align-items: flex-start; gap: 8px; font-size: 14px; color: var(--ink-text); line-height: 19px; }
  .contact-list li.gap { margin-top: 12px; }
  .contact-icon { flex: none; width: 15px; height: 15px; margin-top: 2px; }

  /* Back */
  .card-back { left: 500px; top: 520px; background: var(--card-black); overflow: hidden; }
  .services-title { position: absolute; left: 36px; top: 38px; font-family: "Roboto Slab", Georgia, serif; font-weight: 700; font-size: 36px; color: #fff; }
  .services-list { list-style: none; position: absolute; left: 0; top: 110px; }
  .services-list li { display: flex; align-items: center; height: 34px; font-family: "Roboto Condensed", Arial, sans-serif; font-size: 21px; color: #fff; letter-spacing: .2px; }
  .services-list .swatch { width: 20px; height: 26px; margin-right: 12px; }
  .services-list strong { font-weight: 700; margin-left: 6px; }
  .services-list .lead { font-weight: 700; }
  .paint-splash { position: absolute; right: 0; top: 0; width: 80px; height: 330px; }
</style>
</head>
<body>

<section class="card card-front" aria-label="Business card front">
  <div class="brand-mark">
    <span class="brand-mark__dot"></span>
    <span class="brand-mark__name">Bright Horizon<br>Painting &amp; Remodeling</span>
  </div>
  <div class="divider"></div>
  <div class="details">
    <h1 class="company-name">BRIGHT HORIZON</h1>
    <p class="company-tagline">Painting and Remodeling</p>
    <ul class="contact-list">
      <li>
        <svg class="contact-icon" viewBox="0 0 16 16"><circle cx="8" cy="8" r="8" fill="var(--c-yellow)"/><path d="M5 4.5l1.6-.3.9 2.2-1 .8a6 6 0 0 0 2.3 2.3l.8-1 2.2.9-.3 1.6c-3.5.3-6.8-3-6.5-6.5z" fill="#fff"/></svg>
        (305) 555-0142
      </li>
      <li>
        <svg class="contact-icon" viewBox="0 0 16 16"><circle cx="8" cy="8" r="8" fill="var(--c-orange)"/><rect x="4" y="6" width="8" height="5" rx="1" fill="#fff"/><rect x="5" y="4.5" width="6" height="2" rx="1" fill="#fff"/></svg>
        (855) 555-0197
      </li>
      <li>
        <svg class="contact-icon" viewBox="0 0 16 16"><circle cx="8" cy="8" r="8" fill="var(--c-magenta)"/><rect x="5.5" y="4" width="5" height="3" fill="#fff"/><rect x="4" y="7" width="8" height="4" rx="1" fill="#fff"/></svg>
        (866) 555-0163
      </li>
      <li class="gap">
        <svg class="contact-icon" viewBox="0 0 16 16"><circle cx="8" cy="8" r="8" fill="var(--c-purple)"/><rect x="4" y="5" width="8" height="6" rx="1" fill="#fff"/><path d="M4 5.5l4 3 4-3" stroke="var(--c-purple)" fill="none"/></svg>
        corinne@paintingbrighthorizon.example
      </li>
      <li>
        <svg class="contact-icon" viewBox="0 0 16 16"><circle cx="8" cy="8" r="8" fill="var(--c-blue)"/><path d="M8 3.5a3 3 0 0 1 3 3c0 2.2-3 5.5-3 5.5s-3-3.3-3-5.5a3 3 0 0 1 3-3z" fill="#fff"/><circle cx="8" cy="6.5" r="1.1" fill="var(--c-blue)"/></svg>
        <span>4126 NW 71st st Suite 214<br>Miami, FL 33166</span>
      </li>
    </ul>
  </div>
</section>

<section class="card card-back" aria-label="Business card back">
  <h2 class="services-title">Our Services</h2>
  <ul class="services-list">
    <li><span class="swatch" style="background:var(--s-lime)"></span>INTERIOR AND EXTERIOR<strong style="color:var(--s-lime)">PAINTING</strong></li>
    <li><span class="swatch" style="background:var(--s-yellow)"></span>PRESSURE<strong style="color:var(--s-yellow)">WASHING</strong></li>
    <li><span class="swatch" style="background:var(--s-orange)"></span>DRYWALL AND STUCCO<strong style="color:var(--s-orange)">REPAIR</strong></li>
    <li><span class="swatch" style="background:var(--s-pink)"></span>WALL PAPER/STAINING<strong style="color:var(--s-pink)">REMOVAL</strong></li>
    <li><span class="swatch" style="background:var(--s-blue)"></span><span class="lead">FREE</span><strong style="color:var(--s-blue)">ESTIMATES</strong></li>
  </ul>
  <svg class="paint-splash" viewBox="0 0 80 330" role="img" aria-label="White paint splash decoration along the right edge">
    <path d="M80 20 C55 40 62 80 40 100 C55 130 30 170 45 200 C30 230 50 270 60 300 L80 330 Z" fill="#fff"/>
  </svg>
</section>

</body>
</html>
```